Business Card for Restaurant Vendal

This project consist of creating 2 design for business card of restaurant named Vendal.

The attached specs below are 'ONLY SUGGESTION' if you have others ideas. You are welcome to post it.

1) Restaurant Card

Adresse:
2784 Côte du Pinard Vert
Montréal (Qc) H4K 3T8

Website:
www.ven-dal.ca

Phone:
438-719-2046

2) Employee Card

Name: Lorna Pik
Title: Owner

Address:
2784 Côte du Pinard Vert
Montréal (Qc) H4K 3T8

Email:lorna@ven-dal.ca
Phone Number:438-719-2046
Cellphone Number:514-830-4162

 The attached specs are 'ONLY SUGGESTION' if you have others ideas.  You are welcome to post it.

Industry/Entity Type

Restaurant

Requirements
Must have
• UV Card Spot

To print Spot UV business cards you would have to submit 2 files for each side. The first file "base" would be your regular design file as it would have been in any other case. The 2nd file "UV mask" is a black/white file. The BLACK color will indicate the areas that will be covered with the UV high gloss finish. To upload the files, please combine front design and front mask file in one P
Nice to have
• 1) The font of the logo should be ink effect
2) black background with wallpaper effect
3) The specs below are 'ONLY SUGGESTION' if you have others ideas. You are welcome to post it.

```html
<!DOCTYPE html>
<html lang="fr">
<head>
<meta charset="utf-8">
<title>Vendal – Business Cards</title>
<link href="https://fonts.googleapis.com/css2?family=Lato:wght@400;700;900&display=swap" rel="stylesheet">
<style>
  :root {
    --page-bg: #e9e4dc;
    --card-black: #0c0c0c;
    --lantern-tone: #1b1b1b;
    --brand-red: #e2231a;
    --text-white: #ffffff;
    --text-soft: #e8e8e8;
  }
  * { box-sizing: border-box; margin: 0; padding: 0; }
  html, body {
    width: 1200px; height: 1000px; overflow: hidden;
    background: var(--page-bg);
    font-family: "Lato", Arial, sans-serif;
  }
  .sheet { position: relative; width: 1200px; height: 1000px; }

  .card {
    position: absolute; top: 362px;
    width: 536px; height: 276px;
    background: var(--card-black);
    border-radius: 10px;
    overflow: hidden;
    box-shadow: 0 4px 10px rgba(0,0,0,0.35);
  }
  .card--front { left: 46px; }
  .card--back  { left: 618px; }

  .brand { position: absolute; color: var(--text-white); }
  .brand__row { display: flex; align-items: center; gap: 10px; }
  .brand__name {
    font-weight: 900; font-size: 54px; line-height: 1; letter-spacing: 1px;
    color: var(--text-white);
  }
  .brand__dot {
    width: 30px; height: 30px; border-radius: 50%;
    background: var(--brand-red);
  }
  .brand__tagline {
    margin-top: 8px; font-size: 10.5px; font-weight: 700;
    color: var(--text-soft); letter-spacing: 0.2px;
  }
  .card--front .brand { left: 218px; top: 58px; }
  .card--back .brand  { left: 272px; top: 112px; }

  .lantern {
    position: absolute; border-radius: 48% 48% 45% 45%;
    background: radial-gradient(circle at 40% 35%, #262626, var(--lantern-tone) 70%);
  }
  .card--front .lantern { left: 20px; top: 176px; width: 86px; height: 80px; }
  .card--back .lantern  { left: 37px; top: 60px; width: 176px; height: 172px; transform: rotate(-12deg); }

  .contact-band {
    position: absolute; left: 121px; top: 189px;
    width: 415px; height: 48px;
    background: var(--brand-red);
    clip-path: polygon(0 0, 100% 0, 100% 100%, 0 100%, 22px 50%);
    display: flex; align-items: center;
    padding-left: 40px; gap: 30px;
    color: var(--text-white); font-size: 13.5px; line-height: 18px;
  }
  .contact-band__col { display: flex; flex-direction: column; }
  .contact-line { display: flex; align-items: center; gap: 7px; }
  .contact-line svg { width: 13px; height: 13px; flex: none; }
  .contact-line--indent { padding-left: 20px; }
</style>
</head>
<body>
<main class="sheet">

  <section class="card card--front" aria-label="Carte recto">
    <div class="lantern" role="img" aria-label="Lanterne japonaise en vernis sélectif"></div>
    <div class="brand">
      <div class="brand__row">
        <span class="brand__name">Vendal</span>
        <span class="brand__dot"></span>
      </div>
      <p class="brand__tagline">Resto-Bar Japonais · Izakaya · 居酒屋</p>
    </div>
    <div class="contact-band">
      <div class="contact-band__col">
        <span class="contact-line">
          <svg viewBox="0 0 16 16"><circle cx="8" cy="8" r="7.5" fill="#fff"/><path d="M5 4.5l1.5-.5 1 2-1 .8c.5 1.2 1.4 2.1 2.6 2.6l.8-1 2 1-.5 1.5c-3 .3-6.7-3.4-6.4-6.4z" fill="#e2231a"/></svg>
          438-719-2046
        </span>
        <span class="contact-line">
          <svg viewBox="0 0 16 16"><circle cx="8" cy="8" r="7.5" fill="#fff"/><g fill="none" stroke="#e2231a" stroke-width="1"><circle cx="8" cy="8" r="5"/><ellipse cx="8" cy="8" rx="2.2" ry="5"/><path d="M3 8h10"/></g></svg>
          www.ven-dal.ca
        </span>
      </div>
      <div class="contact-band__col">
        <span class="contact-line">
          <svg viewBox="0 0 16 16"><circle cx="8" cy="8" r="7.5" fill="#fff"/><path d="M8 3.5a3 3 0 0 0-3 3c0 2.3 3 6 3 6s3-3.7 3-6a3 3 0 0 0-3-3z" fill="#e2231a"/><circle cx="8" cy="6.5" r="1.1" fill="#fff"/></svg>
          2784 Côte du Pinard Vert
        </span>
        <span class="contact-line contact-line--indent">Montréal (Qc) H4K 3T8</span>
      </div>
    </div>
  </section>

  <section class="card card--back" aria-label="Carte verso">
    <div class="lantern" role="img" aria-label="Grande lanterne japonaise en vernis sélectif"></div>
    <div class="brand">
      <div class="brand__row">
        <span class="brand__name">Vendal</span>
        <span class="brand__dot"></span>
      </div>
      <p class="brand__tagline">Resto-Bar Japonais · Izakaya · 居酒屋</p>
    </div>
  </section>

</main>
</body>
</html>
```